Upscale business cards needed for family business

We need professional business cards created for several family members. We are a family business holding company. We would like these relatively simple and straightforward, but also with a unique element to set them apart. Probably stick with neutral and simple colors - white, grey etc. We need space for the traditional elements, including name, title, address, email/phone number. And we will be creating several from this template so it needs to be template that is easy to switch information in and out of.

Industry/Entity Type

Business

Contact Information for Business Card

Please include the attached Dunmore Ventures logo.

Requirements
Must have
• The attached Dunmore Ventures logo.

```html
<!DOCTYPE html>
<html lang="en">
<head>
<meta charset="utf-8">
<title>Dunmore Ventures Business Cards</title>
<link href="https://fonts.googleapis.com/css2?family=Roboto:wght@400;500;700&display=swap" rel="stylesheet">
<style>
  :root {
    --page-bg: #e9e7e3;
    --card-dark: #2f2f30;
    --card-dark-deep: #232324;
    --gold: #e6cf6a;
    --gold-light: #f3e59a;
    --gold-deep: #c9ab3e;
    --ink-light: #f2f2f2;
    --ink-muted: #d6d6d6;
  }
  * { margin: 0; padding: 0; box-sizing: border-box; }
  html, body {
    width: 1200px; height: 1023px; overflow: hidden;
    background: var(--page-bg);
    font-family: "Roboto", Arial, sans-serif;
  }
  .sheet {
    width: 1200px; height: 1023px;
    display: flex; flex-direction: column; align-items: center; justify-content: center;
    gap: 56px;
  }
  .card {
    position: relative;
    width: 760px; height: 434px;
    border-radius: 22px;
    overflow: hidden;
    background: radial-gradient(ellipse at 55% 45%, #3a3a3b 0%, var(--card-dark) 45%, var(--card-dark-deep) 100%);
    box-shadow: 0 10px 28px rgba(0,0,0,0.25);
  }

  .gold-panel {
    position: absolute; left: 0; top: 0; bottom: 0; width: 190px;
    background: linear-gradient(160deg, var(--gold-light) 0%, var(--gold) 60%, var(--gold-deep) 100%);
  }

  .brand {
    position: absolute;
    display: flex; align-items: center; gap: 12px;
    color: var(--ink-muted);
    font-weight: 400;
    text-transform: uppercase;
    white-space: nowrap;
  }
  .brand-dot {
    width: 12px; height: 12px; border-radius: 50%;
    background: var(--gold);
    flex: none;
  }
  .brand-rule {
    position: absolute; height: 1px;
    background: linear-gradient(90deg, var(--gold-deep), rgba(201,171,62,0));
  }

  /* Front */
  .front .brand { left: 240px; top: 206px; font-size: 19px; letter-spacing: 2.5px; }
  .front .brand-rule { left: 240px; top: 244px; width: 230px; }

  .person { position: absolute; right: 58px; top: 70px; text-align: right; }
  .person-name { color: #fff; font-weight: 700; font-size: 34px; letter-spacing: 0.5px; }
  .person-title { color: var(--gold); font-size: 17px; margin-top: 2px; }

  .address {
    position: absolute; right: 58px; top: 148px;
    display: flex; gap: 12px; align-items: flex-start;
    color: var(--ink-light); font-size: 16px; line-height: 1.45; text-align: right;
  }
  .address svg { margin-top: 2px; }

  .contacts {
    position: absolute; left: 240px; top: 300px;
    list-style: none;
    color: var(--ink-light); font-size: 17px; line-height: 1;
  }
  .contacts li { display: flex; align-items: center; gap: 14px; margin-bottom: 13px; }
  .contacts svg { flex: none; }

  /* Back */
  .back .brand { left: 50%; top: 178px; transform: translateX(-50%); font-size: 30px; letter-spacing: 4px; }
  .back .brand-rule { left: 230px; top: 236px; width: 300px;
    background: linear-gradient(90deg, rgba(201,171,62,0), var(--gold-deep), rgba(201,171,62,0)); }
  .back-web {
    position: absolute; left: 60px; bottom: 52px;
    color: var(--ink-light); font-size: 17px; letter-spacing: 1.5px;
  }
</style>
</head>
<body>
<main class="sheet">

  <section class="card front" aria-label="Business card front">
    <div class="gold-panel"></div>

    <div class="brand"><span class="brand-dot"></span>Dunmore Ventures</div>
    <div class="brand-rule"></div>

    <div class="person">
      <div class="person-name">Your Name</div>
      <div class="person-title">Title</div>
    </div>

    <div class="address">
      <div>Your address line 1<br>Your address line 2</div>
      <svg width="14" height="18" viewBox="0 0 14 18">
        <path d="M7 0 C3 0 0 3 0 7 C0 12 7 18 7 18 C7 18 14 12 14 7 C14 3 11 0 7 0 Z" fill="var(--gold)"/>
        <circle cx="7" cy="7" r="2.6" fill="var(--card-dark)"/>
      </svg>
    </div>

    <ul class="contacts">
      <li>
        <svg width="16" height="16" viewBox="0 0 16 16"><circle cx="8" cy="8" r="7" fill="none" stroke="var(--gold)" stroke-width="1.5"/><path d="M5.5 4.5 L7 6 L6.2 7 C6.8 8.2 7.8 9.2 9 9.8 L10 9 L11.5 10.5 L10.5 11.5 C8 11 5 8 4.5 5.5 Z" fill="var(--gold)"/></svg>
        88-123-54321
      </li>
      <li>
        <svg width="16" height="12" viewBox="0 0 16 12"><rect x="0.75" y="0.75" width="14.5" height="10.5" fill="none" stroke="var(--gold)" stroke-width="1.5"/><path d="M1 1 L8 7 L15 1" fill="none" stroke="var(--gold)" stroke-width="1.5"/></svg>
        info@yourweb.com
      </li>
      <li>
        <svg width="16" height="16" viewBox="0 0 16 16"><circle cx="8" cy="8" r="7.5" fill="var(--gold)"/><path d="M0.5 8 H15.5 M8 0.5 V15.5 M2 4.5 H14 M2 11.5 H14" stroke="var(--card-dark)" stroke-width="1"/><ellipse cx="8" cy="8" rx="3.5" ry="7.5" fill="none" stroke="var(--card-dark)" stroke-width="1"/></svg>
        www.yourweb.com
      </li>
    </ul>
  </section>

  <section class="card back" aria-label="Business card back">
    <div class="brand"><span class="brand-dot"></span>Dunmore Ventures</div>
    <div class="brand-rule"></div>
    <div class="back-web">www.yourweb.com</div>
  </section>

</main>
</body>
</html>
```